Community coffee table book/quiz book

I need a couple of things for my book:
- Book cover (Title: "1000 gåter om Bakkeskog")
- "Cover pages" for each chapter of the book (15-16 chapters)
- "Watermark" or background design for all the pages of the book.
- A cover image for the book's Facebook page.
- Design of a paper "belt"

The book:
The book will consist of about 200+ pages with ten questions on one page and ten answers on the next.

The name of the book is "1000 gåter om Bakkeskog" which means 1000 questions about Fyllingsdalen (Fyllingsdalen is a suburb of the city Bergen in Norway). Author is Helge Dyrnes.
The questions in the book are grouped in chapters like:
History
Facts
Schools
Businesses
People/profiles
Sport
Culture
Buildings/Landmarks/Sculptures
The different areas of the suburb
The city
Language/expressions
Nature
The names of the chapters are not set, so it would be good to have the option to change the title of the pages without having to contact the designer (maybe by adding the text on top of the cover page?). I therefore suggest that these images are without text.
The book size is 18X18 cm.

The chapter cover pages:
The book will basically consist of text. Ten questions on one page, and ten questions on the next. Visually it will be quite "boring" to look at. I would therefore like to have a chapter cover page for each chapter, preferable in colour.

Water mark:
To avoid having a book full of white pages with limited amount of text I thought of having some kind of design on each page. I do not know how this should be done, but maybe it is possible to create some kind of background image or watermark image with similar design as the book cover and the chapter covers?

The Facebook cover image:
This should be the same as, or similar to, the book cover.
I believe the optimal size is 828px x 315px?

Paper "belt":
The book is to be sold for charity. The receiver of the money is the local sports club. I would like to have the book "wrapped in a 5-6 cm wide paper belt with the logo of the sports club (please see logo and colours here: http://www.ilvarnolia.no). I do not think that the book cover itself should have the sports club's color (purple), but maybe the paper band could? (Again: YOU are the designer)

Photos:
I reckon you would like some photos for both the book cover and the chapter covers. I will of course do the best I can to provide these photos when I have selected a designer. I the meantime

Target Market(s)

Target market is middle clas men and women 35+ from the geographical area Fyllingsdalen.

Industry/Entity Type

Community

Font styles to use
Serif
Sans Serif

Requirements
Must have
• The book will be sold by children on doors. The buyers will probably take a look briefly through the book and then decide if they are going to buy.
• It is important that they like the question types, categories and some of the actual questions they read. But it is also important that they like the look of the book. Therefore the book cover and the chapter cover pages must be appealing enough for the buyers to want this book on theor coffee table.
Nice to have
• I have uploaded a short video clip to Youtube (https://www.klipvista.example/watch?v=qt7Rmx2Lpaw). This a promo clip from Moravel Kids. I felt inspired when I saw it and thought that backgrounds like the ones used in the promo could also be used as backgrounds for each chapter's cover pages. Maybe different colour for each chapter? Screenshots from the clip is uploaded below.
• Then again: Maybe I am an idiot? YOU are the designer :-)
Should not have
• There has been some rivalry between two sportsclubs in the region after the clubs was merged a couple of years ago. I therefore believe we should therefore try avoid both the old clubs' colours (blue&yellow and green) and the new club's colour (purple).

```html
<!DOCTYPE html>
<html lang="no">
<head>
<meta charset="utf-8">
<title>1000 gåter om Bakkeskog – designsett</title>
<link rel="stylesheet" href="https://fonts.googleapis.com/css2?family=Josefin+Sans:wght@300;400&family=Nunito:wght@900&family=Oswald:wght@300&family=Arimo:wght@700&display=swap">
<style>
  :root {
    --pink: #ec008c;
    --pink-deep: #d9007f;
    --yellow: #ffc907;
    --cream: #fddccb;
    --blush: #f8c5d4;
    --page-grey: #f1f1f1;
    --skyline-grey: #e3e3e3;
    --band-grey: #dcdcdc;
    --ink: #111111;
    --white: #ffffff;
  }
  html, body {
    margin: 0;
    padding: 0;
    width: 1200px;
    height: 1000px;
    overflow: hidden;
    background: var(--white);
  }
  .sheet { display: block; width: 1200px; height: 1000px; }
  .fill-pink { fill: var(--pink); }
  .fill-yellow { fill: var(--yellow); }
  .fill-blush { fill: var(--blush); }
  .fill-page { fill: var(--page-grey); }
  .fill-band { fill: var(--band-grey); }
  .count {
    font-family: "Josefin Sans", sans-serif;
    font-weight: 300;
    fill: var(--pink);
    letter-spacing: 10px;
  }
  .title {
    font-family: "Nunito", sans-serif;
    font-weight: 900;
    fill: var(--cream);
  }
  .connector {
    font-family: "Josefin Sans", sans-serif;
    font-weight: 400;
    font-style: italic;
    fill: var(--yellow);
  }
  .place, .chapter-name {
    font-family: "Josefin Sans", sans-serif;
    font-weight: 400;
    fill: var(--yellow);
    letter-spacing: 2px;
  }
  .chapter-name { letter-spacing: 5px; }
  .author {
    font-family: "Josefin Sans", sans-serif;
    font-weight: 400;
    fill: #3a0a26;
  }
  .rule { stroke: var(--white); stroke-width: 1.2; }
  .dots { stroke: var(--yellow); stroke-width: 1.4; stroke-dasharray: 1.5 2.5; }
  .bullet { fill: var(--white); }
  .question {
    font-family: "Arimo", sans-serif;
    font-weight: 700;
    font-size: 10.5px;
    fill: var(--ink);
  }
  .label {
    font-family: "Oswald", sans-serif;
    font-weight: 300;
    font-size: 44px;
    fill: var(--ink);
  }
</style>
</head>
<body>
<svg class="sheet" viewBox="0 0 1200 1000" xmlns="http://www.w3.org/2000/svg">
  <defs>
    <linearGradient id="skyline-pink" x1="0" y1="0" x2="0" y2="1">
      <stop offset="0" stop-color="#d6007e" stop-opacity="0"/>
      <stop offset="0.35" stop-color="#d6007e" stop-opacity="0.55"/>
      <stop offset="1" stop-color="#d6007e" stop-opacity="0.7"/>
    </linearGradient>
    <linearGradient id="skyline-grey" x1="0" y1="0" x2="0" y2="1">
      <stop offset="0" stop-color="#e3e3e3" stop-opacity="0"/>
      <stop offset="0.35" stop-color="#e3e3e3" stop-opacity="0.9"/>
      <stop offset="1" stop-color="#e3e3e3"/>
    </linearGradient>
  </defs>

  <!-- Book cover -->
  <g class="book-cover" transform="translate(45 58)">
    <rect class="fill-yellow" width="397" height="397"/>
    <path class="fill-pink" d="M0,47 C110,14 280,6 397,8 L397,380 L0,380 Z"/>
    <rect x="0" y="270" width="397" height="100" fill="url(#skyline-pink)" role="img" aria-label="Faint city skyline silhouette"/>
    <path class="fill-yellow" d="M0,362 C25,325 80,322 135,346 C220,378 320,382 397,376 L397,397 L0,397 Z"/>
    <rect class="fill-blush" x="128" y="77" width="155" height="66"/>
    <text class="count" x="208" y="132" text-anchor="middle" font-size="60">1000</text>
    <line class="dots" x1="130" y1="151" x2="282" y2="151"/>
    <text class="title" x="200" y="200" text-anchor="middle" font-size="56">Gåter</text>
    <line class="rule" x1="63" y1="219" x2="350" y2="219"/>
    <text class="connector" x="200" y="228" text-anchor="middle" font-size="10">om</text>
    <circle class="bullet" cx="79" cy="242" r="3"/>
    <text class="place" x="200" y="251" text-anchor="middle" font-size="25">BAKKESKOG</text>
    <circle class="bullet" cx="321" cy="242" r="3"/>
    <text class="author" x="200" y="272" text-anchor="middle" font-size="9">Helge Dyrnes</text>
  </g>
  <text class="label" x="246" y="512" text-anchor="middle">BOOK COVER</text>

  <!-- Facebook cover -->
  <g class="facebook-cover" transform="translate(527 182)">
    <rect class="fill-yellow" width="627" height="238"/>
    <path class="fill-pink" d="M0,48 C200,20 450,14 627,18 L627,225 L0,225 Z"/>
    <rect x="0" y="95" width="627" height="120" fill="url(#skyline-pink)" role="img" aria-label="Faint city skyline silhouette"/>
    <path class="fill-yellow" d="M0,200 C30,178 80,180 160,196 C320,222 500,222 627,214 L627,238 L0,238 Z"/>
    <rect class="fill-blush" x="256" y="30" width="141" height="60"/>
    <text class="count" x="331" y="80" text-anchor="middle" font-size="54">1000</text>
    <line class="dots" x1="258" y1="98" x2="396" y2="98"/>
    <text class="title" x="326" y="146" text-anchor="middle" font-size="54">Gåter</text>
    <line class="rule" x1="189" y1="163" x2="461" y2="163"/>
    <text class="connector" x="326" y="172" text-anchor="middle" font-size="10">om</text>
    <circle class="bullet" cx="212" cy="187" r="3"/>
    <text class="place" x="326" y="196" text-anchor="middle" font-size="25">BAKKESKOG</text>
    <circle class="bullet" cx="440" cy="187" r="3"/>
  </g>
  <text class="label" x="853" y="512" text-anchor="middle">FACEBOOK COVER PHOTO</text>

  <!-- Chapter cover: History -->
  <g class="chapter-cover" transform="translate(32 552)">
    <rect class="fill-page" width="348" height="348"/>
    <path class="fill-yellow" d="M0,0 L348,0 L348,28 C240,28 90,30 0,58 Z"/>
    <rect x="0" y="230" width="348" height="100" fill="url(#skyline-grey)" role="img" aria-label="Faint city skyline silhouette"/>
    <path class="fill-yellow" d="M0,320 C25,290 75,292 120,310 C200,340 290,340 348,332 L348,348 L0,348 Z"/>
    <circle class="bullet" cx="91" cy="168" r="3.5"/>
    <text class="chapter-name" x="174" y="178" text-anchor="middle" font-size="27">HISTORY</text>
    <circle class="bullet" cx="267" cy="168" r="3.5"/>
    <line class="dots" x1="100" y1="185" x2="256" y2="185"/>
  </g>

  <!-- Chapter cover: Culture -->
  <g class="chapter-cover" transform="translate(430 552)">
    <rect class="fill-page" width="348" height="348"/>
    <path class="fill-yellow" d="M0,0 L348,0 L348,28 C240,28 90,30 0,58 Z"/>
    <rect x="0" y="230" width="348" height="100" fill="url(#skyline-grey)" role="img" aria-label="Faint city skyline silhouette"/>
    <path class="fill-yellow" d="M0,320 C25,290 75,292 120,310 C200,340 290,340 348,332 L348,348 L0,348 Z"/>
    <circle class="bullet" cx="93" cy="168" r="3.5"/>
    <text class="chapter-name" x="176" y="178" text-anchor="middle" font-size="27">CULTURE</text>
    <circle class="bullet" cx="267" cy="168" r="3.5"/>
    <line class="dots" x1="100" y1="185" x2="256" y2="185"/>
  </g>
  <text class="label" x="392" y="970" text-anchor="middle">COVER PAGES</text>

  <!-- Page background -->
  <g class="page-background" transform="translate(828 552)">
    <rect class="fill-page" width="348" height="348"/>
    <path class="fill-band" d="M0,0 L348,0 L348,28 C240,28 90,30 0,58 Z"/>
    <rect x="0" y="230" width="348" height="100" fill="url(#skyline-grey)" role="img" aria-label="Faint city skyline silhouette"/>
    <path class="fill-band" d="M0,320 C25,290 75,292 120,310 C200,340 290,340 348,332 L348,348 L0,348 Z"/>
    <g class="question-list" text-anchor="middle">
      <text class="question" x="174" y="68">1. Sakldjs asdlkjsd sahjdsdkh sajsdalhksda</text>
      <text class="question" x="174" y="90">2. Asjknddfkj dekjhffjh dskjfhsdfjkhdsfjkhskjsd</text>
      <text class="question" x="174" y="112">3. Qdlkfsjs dslkjfisdfklj sdlkfjdlkfjsdlkfj dksjfldslkj</text>
      <text class="question" x="174" y="134">4. Bsadlkjdlk sljkdslkdj slkjdklajsdl asdksjd</text>
      <text class="question" x="174" y="156">5. Lsdkjhga sadhjgasdhui eguwbn jhewvrlskjueh</text>
      <text class="question" x="174" y="178">6. Wdekjhfs sdkjhffoi edfukiho rouifhoirf</text>
      <text class="question" x="174" y="200">7. Mfjscfkjds dkjshbiu riugfhrgjnb fdndf;lelruhr</text>
      <text class="question" x="174" y="222">8. Bsdklfjsofij dihjfiojf id dfij dfj fodfjdofj fddi</text>
      <text class="question" x="174" y="244">9. Kjdskflkdfsh duhfd hfduhdf difdoiddihd j diud</text>
      <text class="question" x="174" y="266">10. Gslhjkfd sdufhg fiuf dkjhd du fuhyudhuhyuh</text>
    </g>
  </g>
  <text class="label" x="992" y="970" text-anchor="middle">WATERMARK</text>
</svg>
</body>
</html>
```